Business Card Design

I am an Event and Wedding Planner in need of an eye catching business card featuring my logo (attached), my contact details, and my company tagline (Making every milestone simply magnificent...) I would like the tagline in font similar the logo's font.
Updates
I have just noticed that my logo has a misspelling so for the final design, I will be uploading a corrected logo as soon as I have it.
My apologies.
Reason: Waiting on a corrected logo...Occasions is misspelled and it should say Weddings not Wedding
The logo has been corrected so now Occasions is spelled correctly and it says Weddings instead of Wedding. Please use Edwardian Script ITC as the font for the tagline so it will match the logo. Thank you for your patience.
Target Market(s)
Engaged couples and people hosting milestone celebrations. 25-50 years old, predominately female
Industry/Entity Type
Business
Contact Information for Business Card
Rosalind Petty, Event Manager / Owner, Mobile: 0491 837 052, Email: rosalind@glimmerfieldevents.com.au, www.glimmerfieldevents.com.au, Making every milestone simply magnificent...

```html
<!DOCTYPE html>
<html lang="en">
<head>
<meta charset="utf-8">
<title>Glimmerfield Events – Business Card</title>
<link href="https://fonts.googleapis.com/css2?family=Pinyon+Script&family=Tinos:wght@400&display=swap" rel="stylesheet">
<style>
  :root {
    --backdrop: #e6e3df;
    --card-dark: #0f1515;
    --card-dark-edge: #1c2424;
    --card-light: #ffffff;
    --silver: #d4d6d6;
    --silver-soft: #9ea3a3;
    --crimson: #c3202e;
    --crimson-soft: #e58a92;
    --ink: #2a2a2a;
  }
  * { box-sizing: border-box; margin: 0; padding: 0; }
  html, body { width: 1200px; height: 800px; overflow: hidden; }
  body {
    background: var(--backdrop);
    display: flex;
    align-items: center;
    justify-content: center;
    gap: 50px;
  }
  .card {
    width: 540px;
    height: 310px;
    position: relative;
    overflow: hidden;
    box-shadow: 0 10px 28px rgba(0,0,0,0.18);
  }

  /* Back of card */
  .card--back {
    background: linear-gradient(150deg, var(--card-dark-edge), var(--card-dark) 60%);
  }
  .brand {
    position: absolute;
    top: 96px;
    left: 0;
    right: 0;
    display: flex;
    align-items: center;
    justify-content: center;
    gap: 14px;
  }
  .brand__dot {
    width: 14px;
    height: 14px;
    border-radius: 50%;
    background: var(--crimson);
  }
  .brand__name {
    font-family: "Pinyon Script", cursive;
    font-size: 54px;
    color: var(--silver);
    line-height: 1;
  }
  .tagline {
    position: absolute;
    left: 0;
    right: 0;
    bottom: 34px;
    text-align: center;
    font-family: "Pinyon Script", cursive;
    font-size: 28px;
    color: var(--silver-soft);
  }

  /* Front of card */
  .card--front { background: var(--card-light); }
  .holder {
    position: absolute;
    top: 28px;
    left: 32px;
  }
  .holder__name {
    font-family: "Pinyon Script", cursive;
    font-size: 44px;
    color: var(--crimson);
    line-height: 1;
  }
  .holder__role {
    font-family: "Tinos", serif;
    font-size: 14px;
    color: var(--ink);
    margin: 4px 0 0 150px;
  }
  .contact {
    position: absolute;
    top: 104px;
    left: 32px;
    list-style: none;
    font-family: "Tinos", serif;
    font-size: 14px;
    color: var(--ink);
    line-height: 1.55;
  }
  .contact__label {
    color: var(--crimson);
    display: inline-block;
    width: 28px;
  }
  .heart-area {
    position: absolute;
    right: 0;
    bottom: 0;
    width: 250px;
    height: 200px;
    background: radial-gradient(ellipse at 70% 60%, var(--crimson-soft) 0%, rgba(229,138,146,0.25) 55%, rgba(255,255,255,0) 75%);
  }
</style>
</head>
<body>
  <section class="card card--back">
    <div class="brand">
      <span class="brand__dot"></span>
      <span class="brand__name">Glimmerfield Events</span>
    </div>
    <p class="tagline">Making every milestone simply magnificent...</p>
  </section>

  <section class="card card--front">
    <div class="holder">
      <h1 class="holder__name">Rosalind Petty</h1>
      <p class="holder__role">Event Manager | Owner</p>
    </div>
    <ul class="contact">
      <li><span class="contact__label">[P]</span>0491 837 052</li>
      <li><span class="contact__label">[E]</span>rosalind@glimmerfieldevents.com.au</li>
      <li><span class="contact__label">[W]</span>www.glimmerfieldevents.com.au</li>
    </ul>
    <div class="heart-area" role="img" aria-label="Large red brush-stroke heart decoration"></div>
  </section>
</body>
</html>
```